Webdesign for silver path

"Der Sternenpfad" is a new info product that will be selled through the website maybe you will create for us.

Translated from german to english the project is named "the silver path". It´s an online video course that teaches people how to live a fulfilling, happy and healthy life.

Design paramaters
We want a serious design that embodies the real feeling of beeing happy and fulfilled. Visitors should even feel good/better when they see the website.
In color psychology some sort of calming deep green like a four-leaf clover is recommend.
Mainly the website will be the external sales page with a big video as the central attention.
We also need a member area for customers to watch our video course.

So mainly we need a eye-cathing, calming header, the content body with mainly video and just a few written words...and of course a footer for links like imprint, affiliate program etc.

What we not want:
- some kind of these exaggerated smiling photos
- that bathetic luck symbols like money or boats
Updates

Hi,

i posted a message to the design discussion. Thank you!

Industry/Entity Type

Affiliate

```html
<!DOCTYPE html>
<html lang="en">
<head>
<meta charset="utf-8">
<title>The Silver Path</title>
<link rel="stylesheet" href="https://fonts.googleapis.com/css2?family=Fredoka:wght@500;600&family=Ubuntu:wght@500;700&family=Open+Sans:ital,wght@0,400;0,600;1,700&display=swap">
<style>
:root{
  --green:#7cbd0a;
  --green-dark:#5f9a00;
  --green-light:#a6e02a;
  --ink:#3a3a3a;
  --text:#555;
  --muted:#777;
  --page:#fafafa;
  --footer:#efefef;
  --bar:#d8d8d8;
  --player:#1b1a16;
}
*{box-sizing:border-box;margin:0;padding:0}
html,body{width:1200px;height:840px;overflow:hidden}
body{position:relative;background:radial-gradient(ellipse at 70% 30%,#fff 0,#f4f4f4 55%,#ececec 100%);font-family:"Open Sans",sans-serif;color:var(--text)}
.abs{position:absolute}
.top-line{left:0;top:0;width:1200px;height:3px;background:var(--green)}
.call{left:740px;top:11px;display:flex;align-items:center;gap:8px}
.call-icon{width:29px;height:29px;border-radius:6px;background:#1e1e1e;display:flex;align-items:center;justify-content:center}
.call-label{font-family:"Ubuntu",sans-serif;font-weight:700;font-size:14px;color:#333}
.call-number{font-family:"Ubuntu",sans-serif;font-weight:700;font-size:19px;color:var(--green)}
.ribbon{left:1052px;top:0}
.logo{left:158px;top:56px;font-family:"Fredoka",sans-serif;font-weight:600;font-size:42px;color:var(--green)}
.nav{left:631px;top:84px;display:flex;gap:8px}
.nav a{position:relative;display:block;height:32px;padding:0 14px;line-height:32px;border-radius:16px;font-family:"Ubuntu",sans-serif;font-weight:500;font-size:13px;color:#444;text-decoration:none;background:linear-gradient(#f6f6f6,#d9d9d9);box-shadow:0 2px 3px rgba(0,0,0,.15)}
.nav a::after{content:"";position:absolute;left:50%;bottom:-7px;margin-left:-6px;border:6px solid transparent;border-top-color:#d2d2d2;border-bottom:0}
.nav a.active{background:linear-gradient(var(--green-light),var(--green-dark));color:#fff;font-weight:700;padding:0 24px}
.nav a.active::after{border-top-color:var(--green-dark)}
.presenter{left:0;top:196px;width:150px;height:330px;border-radius:40px 40px 10px 10px;background:linear-gradient(#c9cfd8,#8aa0c4 45%,#b9bcbf 75%,#6b6b6b)}
.player{left:127px;top:179px;width:550px;height:360px;background:var(--player);border-radius:4px;box-shadow:0 22px 18px -14px rgba(0,0,0,.25)}
.screen{position:absolute;left:4px;top:4px;width:542px;height:301px;background:linear-gradient(120deg,#d6d0c2,#8a8478 55%,#2a2824)}
.play-big{position:absolute;left:237px;top:116px}
.tip{position:absolute;left:82px;top:282px;width:38px;height:20px;border-radius:3px;background:#eee;font-size:10px;color:#666;text-align:center;line-height:20px}
.track{position:absolute;left:9px;top:308px;width:511px;height:8px;border-radius:4px;background:#5b5a4a}
.track i{position:absolute;left:0;top:0;height:8px;border-radius:4px}
.close{position:absolute;left:526px;top:305px;width:14px;height:14px;background:#3b5a78;color:#cde;font-size:10px;line-height:14px;text-align:center}
.ctrl{position:absolute;top:328px;height:26px;border-radius:3px;background:linear-gradient(#fafafa,#ddd);font-size:10px;color:#888;display:flex;align-items:center;justify-content:center}
.slogan{left:700px;top:176px;font-family:"Fredoka",sans-serif;font-weight:600;font-size:31px;color:var(--green)}
.lead{left:702px;top:224px;width:380px;font-family:"Ubuntu",sans-serif;font-weight:700;font-size:16px;line-height:20px;color:#444}
.intro{left:702px;top:283px;width:380px;font-size:11px;line-height:18px;color:#555}
.intro em{font-weight:700}
.points{left:704px;top:355px;list-style:none;font-size:11px;color:#666}
.points li{height:24px;line-height:18px;padding-left:16px;position:relative}
.points li::before{content:"»";position:absolute;left:0;top:-1px;color:var(--green);font-weight:700;font-size:13px}
.buy{left:706px;top:476px;width:194px;height:52px;border-radius:26px;border:3px solid #fff;background:linear-gradient(var(--green-light),var(--green-dark));box-shadow:0 0 0 1px #9cd13a,0 6px 8px rgba(0,0,0,.18);display:flex;align-items:center;padding-left:24px;gap:16px;font-family:"Ubuntu",sans-serif;font-weight:700;font-size:23px;color:#fff}
.footer{left:0;top:602px;width:1200px;height:202px;background:var(--footer);border-top:2px solid #e2e2e2}
.f-head{font-family:"Fredoka",sans-serif;font-weight:600;font-size:20px;color:var(--green)}
.links{list-style:none;font-size:11px;letter-spacing:.5px;color:#555}
.links li{height:22px;padding-left:17px;position:relative}
.links li::before{content:"";position:absolute;left:1px;top:6px;width:3px;height:3px;border-radius:50%;background:#777}
.social-text{left:814px;top:667px;width:290px;font-size:11px;line-height:18px;font-style:italic;font-weight:700;color:#777}
.social{left:822px;top:727px;display:flex;gap:12px}
.social span{width:44px;height:44px;border-radius:50%;box-shadow:0 2px 3px rgba(0,0,0,.25);border:2px solid #fff}
.copy{left:0;top:804px;width:1200px;height:36px;background:var(--bar);text-align:center;line-height:36px;font-family:Arial,sans-serif;font-size:13px;color:#222}
</style>
</head>
<body>
<div class="abs top-line"></div>

<div class="abs call">
  <span class="call-icon"><svg width="14" height="16" viewBox="0 0 14 16"><path d="M3 1h3l1 4-2 1c1 2 2 4 4 5l1-2 4 1v3c0 1-1 2-2 2C6 15 0 9 1 3c0-1 1-2 2-2z" fill="#fff"/></svg></span>
  <span class="call-label">Call Now !</span>
  <span class="call-number">+1-800-555-0142</span>
</div>
<svg class="abs ribbon" width="22" height="56" viewBox="0 0 22 56"><path d="M0 0h22v46l-11 9-11-9z" fill="#8cc63f"/><circle cx="11" cy="31" r="5" fill="none" stroke="#fff" stroke-width="1.5"/></svg>

<div class="abs logo">The Silver Path</div>

<nav class="abs nav">
  <a class="active" href="#">Home</a>
  <a href="#">About us</a>
  <a href="#">Services</a>
  <a href="#">Courses</a>
  <a href="#">Contact Us</a>
</nav>

<div class="abs presenter" role="img" aria-label="Photo of a presenter standing and gesturing toward the video"></div>

<div class="abs player">
  <div class="screen" role="img" aria-label="Video still: curled film strip beside a camera, sepia toned"></div>
  <svg class="play-big" width="70" height="70" viewBox="0 0 70 70"><circle cx="35" cy="35" r="33" fill="rgba(200,200,200,.55)" stroke="#999" stroke-width="3"/><circle cx="35" cy="35" r="24" fill="#555"/><path d="M29 23l16 12-16 12z" fill="#ddd"/></svg>
  <div class="tip">2:33</div>
  <div class="track"><i style="width:141px;background:#8a8a6a"></i><i style="width:94px;background:var(--green-light)"></i></div>
  <div class="close">✕</div>
  <div class="ctrl" style="left:3px;width:27px"><svg width="9" height="10"><path d="M0 0l9 5-9 5z" fill="#999"/></svg></div>
  <div class="ctrl" style="left:35px;width:65px">2:33 / 9:49</div>
  <div class="ctrl" style="left:104px;width:93px;gap:2px"><svg width="12" height="10"><path d="M0 3h3l4-3v10l-4-3H0z" fill="#888"/></svg>&nbsp;<svg width="60" height="14"><g fill="#7cbd0a"><rect x="0" width="4" height="14" rx="2"/><rect x="6" width="4" height="14" rx="2"/><rect x="12" width="4" height="14" rx="2"/><rect x="18" width="4" height="14" rx="2"/><rect x="24" width="4" height="14" rx="2"/></g><g fill="#ccc"><rect x="30" width="4" height="14" rx="2"/><rect x="36" width="4" height="14" rx="2"/><rect x="42" width="4" height="14" rx="2"/><rect x="48" width="4" height="14" rx="2"/><rect x="54" width="4" height="14" rx="2"/></g></svg></div>
  <div class="ctrl" style="left:422px;width:61px;font-weight:600">SHARE ▾</div>
  <div class="ctrl" style="left:488px;width:27px"><svg width="12" height="12"><path d="M0 0h4M0 0v4M12 0h-4M12 0v4M0 12h4M0 12v-4M12 12h-4M12 12v-4" stroke="#888" stroke-width="2"/></svg></div>
  <div class="ctrl" style="left:520px;width:28px;background:linear-gradient(#d8f78a,#a6e02a);color:#4a6a00;font-weight:600">HD</div>
</div>

<h1 class="abs slogan">Place Your Slogan</h1>
<p class="abs lead">Lorem Ipsum is simply dummy text of the printing and typesetting</p>
<p class="abs intro"><em>Standard dummy text ever since the 1500s, when an unknown printer took a galley of type and scrambled it</em> to make a type specimen book. It has survived not only five centuries,</p>
<ul class="abs points">
  <li>It was popularised in the 1960s with the release of</li>
  <li>Lettrafix sheets containing Lorem Ipsum passages,</li>
  <li>And more recently with desktop publishing software like</li>
  <li>Pagewright Studio including versions of Lorem Ipsum.</li>
</ul>
<a class="abs buy" href="#">Buy Now <svg width="28" height="28" viewBox="0 0 28 28"><circle cx="14" cy="14" r="13" fill="#e8e8e8" stroke="#999"/><path d="M11 8l8 6-8 6z" fill="#555"/></svg></a>

<footer class="abs footer"></footer>
<h2 class="abs f-head" style="left:117px;top:624px">Our Useful Links</h2>
<ul class="abs links" style="left:122px;top:670px"><li>Portrait</li><li>Partnaire</li><li>Informations</li><li>Produits</li><li>Textes Adjudications</li></ul>
<ul class="abs links" style="left:305px;top:670px"><li>Contructions</li><li>References</li><li>Contact</li><li>Links</li><li>Shop</li></ul>
<ul class="abs links" style="left:459px;top:673px"><li>Portrait</li><li>Partnaire</li><li>Informations</li><li>Produits</li><li>Textes Adjudications</li></ul>
<ul class="abs links" style="left:641px;top:673px"><li>Contructions</li><li>References</li><li>Contact</li><li>Links</li><li>Shop</li></ul>
<h2 class="abs f-head" style="left:812px;top:624px">Our Socianl Network</h2>
<p class="abs social-text">Standard dummy text ever since the 1500s, when an unknown printer took a galley</p>
<div class="abs social">
  <span style="background:#3b5a9a"></span>
  <span style="background:#e4e4e4"></span>
  <span style="background:#3aa0d8"></span>
  <span style="background:#f08a1c"></span>
</div>

<div class="abs copy">(c) 2012 ~ The Silver Path ~ All rights reserved.&nbsp; Site powered by Northbeam Studio (www.northbeam-studio.example)</div>
</body>
</html>
```